依頼概要
愛媛県愛南町特産の柑橘「河内晩柑」の果汁100%を沖縄県で「果汁(ジュース)でも割材でも飲める商品」として販売を計画しています。背景には河内晩柑は苦味と酸味のスッキリ味が特徴で甘味がありません。また沖縄は泡盛へ割る飲酒習慣があるほか、通年で暖かくサッパリ味、苦味が好まれる傾向にあるからです。6月に沖縄県で試飲会を行い手応えを得ました。

しかし、沖縄にはシークァーサーがあり、割材=シークァーサーのイメージです。そこでシークァーサーに代わる割材として河内晩柑で需要喚起、市場開拓を狙っています。
つきましては、1/28-1/29に沖縄市の市場にて「河内晩柑100%ジュースの試飲会」と「ラベルデザイン投票」を現地で行います。
当日は720mlと150mlの容器に入ったジュースを用意し、試飲後に沖縄県在住の方が(このラベル=イメージなら買いたい)というラベルデザイン案に票を投じます。

求めているのは「愛媛県愛南町、沖縄県、河内晩柑、割材でも100%果汁でもおいしく飲めるお得感」というイメージを盛り込んだラベルデザインです。容器は720mlと150mlの2種類ですが、150mlのデザインを150%拡大して720mlに流用します。なので依頼は一種類のラベルデザインです。

投票で票を最多獲得したラベルデザイン案を採用しますが、投票後に寄せられた意見を元に軽度なブラッシュアップ(例:色味、レイアウト、線種など)があることを想定しています。予めご了承ください。

愛南町河内晩柑ホームページ
https://www.sakurane-shiki.example/nousan/osusume/kajitsu/hoshizora/minorikan.html

*追加情報がある場合は加筆させていただきます。

<依頼内容>
・沖縄県で「100%果汁」でも「割材」としても販売する愛媛県愛南町河内晩柑100%果汁のラベルデザイン
・ラベルデザインサイズは150mlが「W:40mm、H:80mm」の範囲内、720mlは150mlのデザインを150%拡大します。
・複雑な形で細かい切り抜き設定が必要なラベルデザインも可能ですが、シールの形状は扱いやすい楕円や四角などのデザインが好みです。
・期待するラベルデザインは、「愛媛県愛南町、沖縄県、河内晩柑、割材でも100%ジュースでもおいしく飲めるお得感」というイメージを盛り込んだものです。コラボデザインもイメージになります。
・ラベルデザインの表記は「漢字、ひらがな、カタカナ、英語表記など」問いませんが、沖縄県の方が「欲しい」という需要の喚起ができるようお願いします。
・1/28-1/29に沖縄県沖縄市の「ゆいまわる市場」にて試飲会と試飲参加者を対象にしたラベルデザインコンテスト(投票)を行います。
・デザインの決定は1月末の予定です。
・1/28-1/29のラベルデザインコンテンスト時に投票者から色味やレイアウトなど軽度な変更を依頼された場合は修正をお願いする可能性があります。
・納品はイラストレーター形式の場合、CS6の古いバージョンでのファイルをお願いします。またPDFでも提供願います。
・ご提案いただくラベルデザイン案には創作意図などを添えていただくと幸いです。
(11/25)表現を正確にしました。
甘みが無いと表記しましたが、正確には「甘みと酸味のバランスの良いさわやかな味でほのかな苦味が特徴」です。

(11/25)写真と2点(150ml瓶、河内晩柑を切った断面)追加しました。
【追記(12/10)】
この度は、ご提案いただき、ありがとうございました。素敵なデザイン案が届き始めました。
そこで一点の再考をお願いします。
今回の依頼は「沖縄県で販売する河内晩柑100%果汁」です。ご提案いたいたデザイン案の多くはキーワードの一つである「沖縄県での販売」という訴求ポイントが欠けている気がします。
ご提案のデザインの多くは、沖縄県外でも売れる気がしますが、狙っているのは「沖縄県」です。
参考までに追記いたします。
【追記:12月31日】
この度は、愛媛県愛南町産の河内晩柑100%果汁のラベルデザインへの提案をありがとうございました。
全てのデザイン案を愛南町と精査している最中です。
そしてツクリエルさんとも協議し、1/28-1/29に沖縄県沖縄市にある「みどり南風産直センター_ゆいまわる〜市場」にて来場者による投票でデザインを決定するため、最終選定日を1/31にさせていただくことになりました。
しばらく時間を要しますが、ご容赦ください。よろしくお願いします。

この度は「愛媛県愛南町河内晩柑100%果汁」のラベルデザインへのご参加、ありがとうございました。
1/28-1/29に沖縄県沖縄市にある「ゆいまわる〜市場」にて投票を行い、計276人が参加しました。
その結果、「愛南町(愛媛県)と沖縄のイメージが上手に融合した」と評されたデザインが最多得票となりました。

大変、長らくお待たせして恐縮ですが、重ねてのご参加、ありがとうございました。
一つ一つのデザインに理由や背景があることがわかりました。
また、このような機会がありましたら、ご案内したいと思います。

```html
<!DOCTYPE html>
<html lang="ja">
<head>
<meta charset="utf-8">
<title>河内晩柑 果汁100% ラベル</title>
<link rel="stylesheet" href="https://fonts.googleapis.com/css2?family=Yuji+Boku&family=Zen+Maru+Gothic:wght@700&display=swap">
<style>
  :root {
    --page-bg: #ecebe8;
    --label-bg: #ffffff;
    --ink: #2b2622;
    --citrus: #f2b24a;
    --citrus-light: #fbd48f;
    --shisa: #8a5a2e;
    --panel-dark: #3a3d44;
    --juice-text: #f0a432;
    --panel-text: #ffffff;
  }
  * { margin: 0; padding: 0; box-sizing: border-box; }
  html, body {
    width: 1200px;
    height: 2392px;
    overflow: hidden;
    background: var(--page-bg);
  }
  .label {
    position: absolute;
    left: 220px;
    top: 246px;
    width: 760px;
    height: 1900px;
    background: var(--label-bg);
    box-shadow: 0 0 0 2px #d8d6d1;
    overflow: hidden;
  }
  .fruit-scatter {
    position: absolute;
    left: 0;
    top: 60px;
    width: 760px;
    height: 640px;
    background: radial-gradient(ellipse at 50% 40%, var(--citrus-light) 0%, rgba(251,212,143,0.55) 45%, rgba(255,255,255,0) 75%);
  }
  .title {
    position: absolute;
    writing-mode: vertical-rl;
    font-family: "Yuji Boku", serif;
    color: var(--ink);
    line-height: 1;
  }
  .title-origin {
    left: 410px;
    top: 300px;
    font-size: 88px;
    letter-spacing: 2px;
  }
  .title-name {
    left: 235px;
    top: 450px;
    font-size: 112px;
    letter-spacing: 4px;
  }
  .title-name .emph {
    text-emphasis: filled dot var(--citrus);
    -webkit-text-emphasis: filled dot var(--citrus);
  }
  .badge {
    position: absolute;
    left: 0;
    width: 200px;
    background: var(--panel-dark);
    font-family: "Zen Maru Gothic", sans-serif;
    font-weight: 700;
    display: flex;
    flex-direction: column;
    justify-content: center;
    align-items: center;
    line-height: 1.15;
  }
  .badge-juice {
    top: 1180px;
    height: 250px;
    color: var(--juice-text);
    font-size: 52px;
  }
  .badge-mixer {
    top: 1510px;
    height: 310px;
    color: var(--panel-text);
    font-size: 62px;
  }
  .shisa {
    position: absolute;
    left: 230px;
    top: 1130px;
    width: 470px;
    height: 630px;
    background: radial-gradient(ellipse at 50% 55%, var(--shisa) 0%, rgba(138,90,46,0.75) 50%, rgba(255,255,255,0) 78%);
  }
</style>
</head>
<body>
  <section class="label">
    <div class="fruit-scatter" role="img" aria-label="散らばる河内晩柑の実と葉のイラスト"></div>
    <h1 class="title title-origin">愛媛県特産の柑橘</h1>
    <p class="title title-name">「<span class="emph">河内晩柑</span>」</p>
    <div class="badge badge-juice"><span>果汁</span><span>100%</span></div>
    <div class="badge badge-mixer"><span>割材</span><span>OK</span></div>
    <div class="shisa" role="img" aria-label="沖縄のシーサーのイラスト"></div>
  </section>
</body>
</html>
```